Need 3 posters for in-store display

Hi Marla,

Hope you are well.
I need 3 posters for display in my restaurant.

Poster 1: To be print in A1 size vertical
Title: BOWL-ERIFIC DEAL $19.50
Choose any Pho OR Noodle Salads
Choose Spring Rolls (5 rolls) OR Ricepaper Rolls (2 rolls)
Choose any Cans OR Water

What I like to see:
- These poster will be place near my counter so I want it to grab customer attention.
- You must use photos to show products
- Make it easy to understand and for customer to follow

Poster 2: To be print in A4 size vertical
Title: ADD TO YOUR ORDER
SpringRolls (Crab / vegetarian) $6 / 5 rolls
Extra Meat $2
Extra Noodles $1
Extra Vegs $1.5
Extra Tofu $2
Extra Crackling $3

Poster 3: To be print in A1 size vertical
Title: BROTH BONANZA FEAST
Catering Menu Options:
- PHO (Beef, Chicken, Vegan) $12.50 per bowl
- NOODLE SALADS (Beef, Chicken, BBQ Pork, Vegan) $12.50 per bowl
- SpringRolls (Crab / vegetarian) $12.50 for 10 rolls
- Ricepaper Rolls (Prawn, Beef, Chicken, BBQ Pork, Tofu) $12.5 / 5 rolls
- Fried Rice (Prawn, Tofu) $50 per tray (serve 5-6)

Terms & Conditions for All Catering Orders:
1) Minimum orders $200 (Pick-Up from shop Only)
2) All orders must be paid upfront
3) Requires $300 bond for Soup Tank
4) Please give us 48hours notice

• For the BOWL-ERIFIC DEAL
• it would be nice to have an image of the battle of water to visually complete the meal deal
• please see attachment of the Cedar Ridge Water

```html
<!DOCTYPE html>
<html lang="en">
<head>
<meta charset="utf-8">
<title>Add To Your Order</title>
<link rel="stylesheet" href="https://fonts.googleapis.com/css2?family=Oswald:wght@700&family=Open+Sans:wght@400;700&display=swap">
<style>
  :root {
    --black: #000000;
    --maroon-top: #3a0203;
    --maroon-bottom: #120000;
    --gold-light: #f3d27a;
    --gold: #d9a93a;
    --gold-dark: #b8862a;
    --lime: #b6cc1e;
    --white: #ffffff;
    --footer-ink: #3a2c10;
  }
  * { margin: 0; padding: 0; box-sizing: border-box; }
  html, body { width: 872px; height: 1200px; overflow: hidden; background: var(--black); }
  .poster { position: relative; width: 872px; height: 1200px; overflow: hidden; font-family: "Open Sans", sans-serif; }

  .header { position: absolute; left: 0; top: 0; width: 872px; height: 235px; background: var(--black); }
  .title {
    position: absolute; left: 0; width: 872px; top: 50px; text-align: center;
    font-family: "Oswald", sans-serif; font-weight: 700; font-size: 68px; line-height: 1;
    letter-spacing: 2px;
    background: linear-gradient(180deg, var(--gold-light) 0%, var(--gold) 55%, var(--gold-dark) 100%);
    -webkit-background-clip: text; background-clip: text; color: transparent;
  }
  .feature-box {
    position: absolute; left: 63px; top: 135px; width: 697px; height: 49px;
    border: 1.5px solid var(--white);
    display: flex; align-items: center; justify-content: center;
    color: var(--white); font-weight: 700; font-size: 23px; letter-spacing: 0.3px;
  }

  .extras { position: absolute; left: 0; top: 235px; width: 872px; height: 362px;
    background: linear-gradient(180deg, var(--maroon-top) 0%, #240000 60%, var(--maroon-bottom) 100%); }
  .extras-label {
    position: absolute; left: 143px; top: 558px; width: 290px; height: 72px;
    transform: rotate(-90deg); transform-origin: 0 0;
    font-family: "Oswald", sans-serif; font-weight: 700; font-size: 92px; line-height: 72px;
    letter-spacing: 1px; text-align: center; white-space: nowrap;
    background: linear-gradient(90deg, var(--gold-dark), var(--gold-light) 50%, var(--gold));
    -webkit-background-clip: text; background-clip: text; color: transparent;
  }
  .extras-list { position: absolute; left: 226px; top: 32px; width: 506px; list-style: none; }
  .extras-item { display: flex; align-items: baseline; height: 60.5px; }
  .item-name { color: var(--white); font-size: 55px; line-height: 60px; letter-spacing: -0.5px; }
  .leader { flex: 1; height: 5px; margin: 0 3px 0 2px;
    background-image: radial-gradient(circle, var(--gold-light) 1.8px, transparent 2.1px);
    background-size: 10px 5px; background-repeat: repeat-x; }
  .item-price { color: var(--lime); font-weight: 700; font-size: 50px; line-height: 60px; width: 110px; }

  .photo { position: absolute; left: 0; top: 597px; width: 872px; height: 523px; }

  .footer { position: absolute; left: 0; top: 1120px; width: 872px; height: 80px;
    background: linear-gradient(90deg, var(--gold-dark) 0%, var(--gold-light) 45%, #f6d98a 70%, var(--gold) 100%);
    display: flex; align-items: center; justify-content: space-between; padding: 0 44px 0 43px;
    color: var(--footer-ink); font-size: 23px; }
  .web { display: flex; align-items: center; gap: 12px; }
</style>
</head>
<body>
<div class="poster">
  <header class="header">
    <h1 class="title">ADD TO YOUR ORDER</h1>
    <div class="feature-box">SPRINGROLLS (CRAB / VEGETARIAN) $6 / 5 ROLLS</div>
  </header>

  <section class="extras">
    <ul class="extras-list">
      <li class="extras-item"><span class="item-name">MEAT</span><span class="leader"></span><span class="item-price">$2</span></li>
      <li class="extras-item"><span class="item-name">NOODLES</span><span class="leader"></span><span class="item-price">$1</span></li>
      <li class="extras-item"><span class="item-name">VEGS</span><span class="leader"></span><span class="item-price">$1.5</span></li>
      <li class="extras-item"><span class="item-name">TOFU</span><span class="leader"></span><span class="item-price">$2</span></li>
      <li class="extras-item"><span class="item-name">CRACKLING</span><span class="leader"></span><span class="item-price">$3</span></li>
    </ul>
  </section>
  <div class="extras-label">EXTRA</div>

  <svg class="photo" role="img" aria-label="Photo of golden fried spring rolls with a prawn, herbs and chopsticks on a dark stone surface" viewBox="0 0 872 523" preserveAspectRatio="none">
    <defs>
      <radialGradient id="food-glow" cx="0.55" cy="0.6" r="0.55">
        <stop offset="0" stop-color="#c99a4e"/>
        <stop offset="0.45" stop-color="#7a5a32"/>
        <stop offset="1" stop-color="#2c2e30"/>
      </radialGradient>
    </defs>
    <rect width="872" height="523" fill="url(#food-glow)"/>
  </svg>

  <footer class="footer">
    <span class="phone">Call Us:0400 555 218</span>
    <span class="web">
      <svg width="30" height="30" viewBox="0 0 30 30" aria-hidden="true">
        <g fill="none" stroke="#1c1508" stroke-width="1.6">
          <circle cx="15" cy="15" r="13"/>
          <circle cx="15" cy="15" r="9"/>
          <ellipse cx="15" cy="15" rx="4" ry="9"/>
          <line x1="6" y1="15" x2="24" y2="15"/>
          <line x1="7.5" y1="10.5" x2="22.5" y2="10.5"/>
          <line x1="7.5" y1="19.5" x2="22.5" y2="19.5"/>
        </g>
      </svg>
      www.brothandbowl.com
    </span>
  </footer>
</div>
</body>
</html>
```